Infographic - 360 degree feedback

We require an infographic design for a product/service offering called 360 degree feedback. The purpose of the infographic is to summarise what 360 degree feedback is as well as entice the prospective client to enquire about the product/service.
Target Market(s)
Government, council and commercial industry sectors
Industry/Entity Type
Recruitment
Font styles to use
Serif
Sans Serif
Colors
Designer to choose colors to be used in the design.
Requirements
Must have
- Color, simple, to the point and summarise the key points of the service offering

```html
<!DOCTYPE html>
<html lang="en">
<head>
<meta charset="utf-8">
<title>360 Degree Feedback Infographic</title>
<link href="https://fonts.googleapis.com/css2?family=Righteous&family=Open+Sans:ital,wght@0,400;0,600;0,700;1,400&display=swap" rel="stylesheet">
<style>
  :root {
    --page: #ececec;
    --sheet-top: #ffffff;
    --sheet-bottom: #e9edf1;
    --title-red: #e2475a;
    --magenta: #c42a8f;
    --pink: #d6399a;
    --orange: #ec6e5a;
    --purple: #8e4aa6;
    --blue: #3fb6e0;
    --green: #a5d36d;
    --salmon: #e8806a;
    --grey-text: #7b7b7b;
    --grey-box: #bfbfbf;
    --grey-num: #b5b5b5;
    --grey-emblem: #dcdcdc;
    --rule: #c8c8c8;
  }
  * { margin: 0; padding: 0; box-sizing: border-box; }
  html, body { width: 1200px; height: 1000px; overflow: hidden; background: var(--page); }
  body { font-family: "Open Sans", Arial, sans-serif; position: relative; }

  .infographic {
    position: absolute; left: 0; top: 161px;
    width: 1200px; height: 678px;
    background: linear-gradient(120deg, var(--sheet-top) 0%, var(--sheet-top) 45%, var(--sheet-bottom) 100%);
    overflow: hidden;
  }
  .connectors { position: absolute; left: 0; top: 0; }

  /* Intro column */
  .intro { position: absolute; left: 142px; top: 105px; width: 186px; }
  .intro__kicker { font-family: "Righteous", sans-serif; font-size: 17px; color: var(--grey-text); }
  .intro__kicker span { color: var(--title-red); }
  .intro__title { font-family: "Righteous", sans-serif; font-size: 33px; line-height: 34px; color: var(--title-red); margin-top: 2px; }
  .intro__text { font-size: 9px; line-height: 12.5px; color: var(--magenta); margin-top: 12px; }
  .intro__note { font-size: 6.5px; line-height: 8.5px; color: var(--grey-text); margin-top: 10px; }

  .emblem { position: absolute; left: 150px; top: 440px; width: 112px; height: 112px;
    border-radius: 8px; background: var(--grey-emblem); }

  .divider { position: absolute; left: 332px; top: 106px; width: 3px; height: 466px;
    background: linear-gradient(var(--magenta), var(--purple) 50%, var(--blue)); }

  /* Types column */
  .types { position: absolute; left: 346px; top: 106px; width: 222px; color: var(--grey-text); }
  .types__lead { font-size: 10px; line-height: 13px; }
  .types__lead em { font-style: italic; }
  .type { margin-top: 12px; }
  .type__head { display: flex; height: 22px; }
  .type__num { width: 22px; background: var(--grey-num); color: #fff; font-size: 12px; font-weight: 700; display: flex; align-items: center; justify-content: center; }
  .type__name { flex: 1; margin-left: 3px; color: #fff; font-size: 11px; font-weight: 700; display: flex; align-items: center; justify-content: center; }
  .type--normative .type__name { background: var(--salmon); }
  .type--competency .type__name { background: var(--green); }
  .type__text { font-size: 9.5px; line-height: 12.5px; margin-top: 6px; }
  .type--competency { margin-top: 36px; }

  .question-rule { position: absolute; left: 572px; top: 135px; width: 1px; height: 390px; background: var(--rule); }
  .question { position: absolute; left: 574px; top: 292px; width: 112px; height: 92px; background: var(--grey-box);
    color: #fff; font-size: 10px; font-weight: 600; line-height: 12px; padding: 12px 6px; }

  /* Benefits */
  .benefit-icon { position: absolute; width: 84px; height: 84px; border-radius: 50%; background: #f4f4f4;
    box-shadow: 0 3px 8px rgba(0,0,0,0.25); display: flex; align-items: center; justify-content: center; }
  .benefit-icon__fill { width: 64px; height: 64px; border-radius: 50%; }
  .benefit-icon--pink { left: 658px; top: 118px; } .benefit-icon--pink .benefit-icon__fill { background: var(--pink); }
  .benefit-icon--orange { left: 693px; top: 238px; } .benefit-icon--orange .benefit-icon__fill { background: var(--orange); }
  .benefit-icon--purple { left: 693px; top: 358px; } .benefit-icon--purple .benefit-icon__fill { background: var(--purple); }
  .benefit-icon--blue { left: 658px; top: 478px; } .benefit-icon--blue .benefit-icon__fill { background: var(--blue); }

  .benefit { position: absolute; left: 862px; width: 196px; }
  .benefit__label { display: inline-block; color: #fff; font-size: 9px; font-weight: 700; padding: 2px 6px; width: 196px; text-align: center; }
  .benefit__text { font-size: 9.5px; line-height: 12.5px; margin-top: 4px; }
  .benefit--pink { top: 120px; } .benefit--pink .benefit__label { background: var(--pink); } .benefit--pink .benefit__text { color: var(--pink); }
  .benefit--orange { top: 242px; } .benefit--orange .benefit__label { background: var(--orange); } .benefit--orange .benefit__text { color: var(--orange); }
  .benefit--purple { top: 362px; } .benefit--purple .benefit__label { background: var(--purple); } .benefit--purple .benefit__text { color: var(--purple); }
  .benefit--blue { top: 482px; } .benefit--blue .benefit__label { background: var(--blue); } .benefit--blue .benefit__text { color: var(--blue); }
</style>
</head>
<body>
<main class="infographic">

  <svg class="connectors" width="1200" height="678" viewBox="0 0 1200 678" aria-hidden="true">
    <defs>
      <linearGradient id="arc-grad" x1="0" y1="0" x2="0" y2="1">
        <stop offset="0" stop-color="#d6399a"/>
        <stop offset="0.5" stop-color="#8e4aa6"/>
        <stop offset="1" stop-color="#3fb6e0"/>
      </linearGradient>
    </defs>
    <path d="M 640 90 Q 770 340 640 590" fill="none" stroke="url(#arc-grad)" stroke-width="3"/>
    <path d="M 690 40 Q 900 340 690 640" fill="none" stroke="url(#arc-grad)" stroke-width="3"/>
    <g stroke-width="1.2">
      <line x1="757" y1="160" x2="860" y2="128" stroke="#d6399a"/>
      <line x1="791" y1="280" x2="860" y2="250" stroke="#ec6e5a"/>
      <line x1="791" y1="400" x2="860" y2="370" stroke="#8e4aa6"/>
      <line x1="757" y1="520" x2="860" y2="490" stroke="#3fb6e0"/>
    </g>
    <g fill="#ffffff" stroke-width="3">
      <circle cx="757" cy="160" r="5" stroke="#d6399a"/>
      <circle cx="791" cy="280" r="5" stroke="#c43b8e"/>
      <circle cx="791" cy="400" r="5" stroke="#8e4aa6"/>
      <circle cx="757" cy="520" r="5" stroke="#3fb6e0"/>
    </g>
  </svg>

  <section class="intro">
    <p class="intro__kicker">Intro<span>ducing</span></p>
    <h1 class="intro__title">360<br>Degree<br>Feedback</h1>
    <p class="intro__text">360 degree feedback is a powerful tool designed to assess individual, group and organisational performance, and most importantly, leadership behaviours.</p>
    <p class="intro__text">Designed in collaboration with Harbourne University, this 30 question short questionnaire provides you with the chance to compare the results of your staff our normative sample* to ensure feedback is accurate.</p>
    <p class="intro__note">*Normative sample consists of over 1000 Australian leaders from the general population.</p>
  </section>

  <div class="emblem" role="img" aria-label="360 degree feedback emblem"></div>

  <div class="divider"></div>

  <section class="types">
    <p class="types__lead">There are two types of<br><em>360 degree feedback</em><br>instruments that can be used</p>
    <article class="type type--normative">
      <div class="type__head"><span class="type__num">1</span><span class="type__name">NORMATIVE</span></div>
      <p class="type__text">Based on standard questions that have been developed and normed across thousands of 360 degree feedback projects. The strength of this approach is that if the tool is developed well the results will give you immediate comparisons to other groups of employees, so people will know whether they are above or below average on each measure.</p>
    </article>
    <article class="type type--competency">
      <div class="type__head"><span class="type__num">2</span><span class="type__name">COMPETENCY BASED</span></div>
      <p class="type__text">Based on unique questions that we develop for a particular group. Talvera often does this through workshop activities, working with the group to be assessed to develop a list of key behaviours that they believe are critical to success. We then turn these key behaviours into 360 degree feedback questions and administer the questions using our Talvera 360 software. The advantage of this approach is that it tends to bring about more significant change than normative instruments do, and people tend to be engaged with the approach.</p>
    </article>
  </section>

  <div class="question-rule"></div>
  <p class="question">What will the 360 degree feedback help me address and benefit my organisation?</p>

  <div class="benefit-icon benefit-icon--pink"><div class="benefit-icon__fill" role="img" aria-label="Icon of a single leader"></div></div>
  <div class="benefit-icon benefit-icon--orange"><div class="benefit-icon__fill" role="img" aria-label="Icon of two staff members"></div></div>
  <div class="benefit-icon benefit-icon--purple"><div class="benefit-icon__fill" role="img" aria-label="Icon of a research document"></div></div>
  <div class="benefit-icon benefit-icon--blue"><div class="benefit-icon__fill" role="img" aria-label="Icon of a group of leaders"></div></div>

  <article class="benefit benefit--pink">
    <h2 class="benefit__label">LEADERSHIP BEHAVIOURS</h2>
    <p class="benefit__text">Crucial for maintaining engagement in the organisation, research shows that an increase in engagement from your leaders correlates to an increase in productivity</p>
  </article>
  <article class="benefit benefit--orange">
    <h2 class="benefit__label">STAFF ENGAGEMENT</h2>
    <p class="benefit__text">Leadership behaviours have proven to be good predictors of staff engagement as it is a strong driver in engagement of human beings</p>
  </article>
  <article class="benefit benefit--purple">
    <h2 class="benefit__label">BACKED BY RESEARCH</h2>
    <p class="benefit__text">Talvera has partnered up with Harbourne University to build a questionnaire based on 30 questions proven to be mathematically pure in measuring 10 leadership characteristics</p>
  </article>
  <article class="benefit benefit--blue">
    <h2 class="benefit__label">IDENTIFY WHO YOUR LEADERS ARE</h2>
    <p class="benefit__text">Our measurement tool will help you identify leaders who are strong in creating clarity in performance standards and provide reports which show key learnings amongst your group of leaders</p>
  </article>

</main>
</body>
</html>
```